Healthcare Recruitment Agency Brochure

We need our current Brochure updated as its old and dated. The brochure will be for our current and potential Clients and should provide all the necessary information regarding our services, but in a well presented, easy reading format which echoes our company Brand. The company supplies Healthcare establishments with trained healthcare Staff which can be in a variety of settings.
UPDATE: Following the submission of many designs we would like to amend the information/content to be included in the brochure and have uploaded additional information. We would like an 8 page booklet with the various sections spread out so as not to look to 'wordy' page 1 Front cover, 2 About Us, 3 Our Service, 4 Our promise, 5 Our Staff, 6 Our Ethos, 7 What Our Clients Say/Testimonials, 8 Contact Us/Back page. Please if using pictures (which is welcomed) steer away from the surgical/doctor type. We mainly provide care to the Elderly within Nursing and Residential Homes and Support Environments. Thanks
Updates

Target Market(s)

Healthcare clientell

Industry/Entity Type

Healthcare

Requirements
Must have
• Pictures, animation, easy reading, informative, tie in with website theme www.carewellstaffline.example
Nice to have
• open to ideas
Should not have
• very long text paragraphs

```html
<!DOCTYPE html>
<html lang="en">
<head>
<meta charset="utf-8">
<title>Our Staff – Carewell Staffline</title>
<link rel="stylesheet" href="https://fonts.googleapis.com/css2?family=Raleway:wght@400;500&family=Baloo+2:wght@800&display=swap">
<style>
  :root {
    --brand-blue: #1577bf;
    --brand-green: #17a98e;
    --ink: #1d1d1d;
    --paper: #ffffff;
    --body-font: "Raleway", Arial, sans-serif;
    --title-font: "Baloo 2", "Arial Rounded MT Bold", sans-serif;
  }
  * { margin: 0; padding: 0; box-sizing: border-box; }
  html, body { width: 777px; height: 1200px; overflow: hidden; background: var(--paper); }
  .page {
    position: relative; width: 777px; height: 1200px; overflow: hidden;
    font-family: var(--body-font); color: var(--ink); background: var(--paper);
  }
  .top-band { position: absolute; top: 0; left: 0; width: 777px; height: 46px; display: flex; }
  .band-blue { background: var(--brand-blue); width: 461px; height: 100%; }
  .band-green { background: var(--brand-green); flex: 1; height: 100%; }

  .page-title {
    position: absolute; left: 103px; top: 86px;
    font-family: var(--title-font); font-weight: 800; font-size: 50px; line-height: 1;
    letter-spacing: 0.5px;
  }
  .page-title .word-our { color: var(--brand-blue); }
  .page-title .word-staff { color: var(--brand-green); }
  .title-rule {
    position: absolute; left: 30px; top: 152px; width: 388px; height: 2.5px;
    background: var(--brand-green);
  }

  .brand-name {
    position: absolute; left: 505px; top: 108px; width: 250px;
    display: flex; align-items: center; gap: 10px;
    font-family: var(--body-font); font-weight: 500; font-size: 26px; color: var(--brand-blue);
  }
  .brand-dot { width: 16px; height: 16px; border-radius: 50%; background: var(--brand-green); flex: none; }

  .photo-strip { position: absolute; top: 192px; left: 0; width: 777px; height: 146px; display: flex; }
  .strip-blue { background: var(--brand-blue); width: 416px; height: 100%; }
  .strip-green { background: var(--brand-green); flex: 1; height: 100%; }
  .photo { position: absolute; top: 13px; height: 120px; }
  .photo-garden { left: 20px; width: 395px; background: linear-gradient(100deg, #6f9a4a 0%, #a9c98a 40%, #d9b49a 60%, #5d8a3a 100%); }
  .photo-flowers { left: 417px; width: 350px; background: linear-gradient(100deg, #5f7d3c 0%, #8fb0d9 40%, #d8c08a 70%, #e5c84a 100%); }

  .copy { position: absolute; left: 32px; width: 735px; font-size: 17.6px; line-height: 21px; }
  .intro { top: 385px; }
  .checklist { list-style: none; }
  .checklist li { position: absolute; left: 32px; width: 735px; font-size: 17.6px; line-height: 22px; }
  .checklist .num { color: var(--brand-green); font-weight: 500; }
  .closing-a { top: 1010px; }
  .closing-b { top: 1107px; }

  .footer-band { position: absolute; bottom: 0; left: 0; width: 777px; height: 29px; display: flex; }
  .footer-text {
    position: absolute; bottom: 0; left: 0; width: 777px; height: 29px;
    display: flex; align-items: center; justify-content: center;
    color: #fff; font-size: 11.4px;
  }
</style>
</head>
<body>
<main class="page">
  <div class="top-band"><div class="band-blue"></div><div class="band-green"></div></div>

  <h1 class="page-title"><span class="word-our">OUR</span> <span class="word-staff">STAFF</span></h1>
  <div class="title-rule" aria-hidden="true"></div>

  <div class="brand-name"><span class="brand-dot"></span>Carewell Staffline</div>

  <div class="photo-strip"><div class="strip-blue"></div><div class="strip-green"></div>
    <div class="photo photo-garden" role="img" aria-label="A carer pushing a smiling elderly woman in a wheelchair along a garden path"></div>
    <div class="photo photo-flowers" role="img" aria-label="A carer with an elderly man in a wheelchair beside a flower bed"></div>
  </div>

  <p class="copy intro">All our candidates go through a thorough vetting and recruitment process and only ever commence assignments after the following :</p>

  <ol class="checklist">
    <li style="top:453px"><span class="num">1.</span> A face-to-face interview and skills assessment has been undertaken.</li>
    <li style="top:510px"><span class="num">2.</span> Full employment history has been submitted</li>
    <li style="top:567px"><span class="num">3.</span> Right to work has been recorded and verified.</li>
    <li style="top:623px"><span class="num">4.</span> Fitness to work has been declared.</li>
    <li style="top:680px"><span class="num">5.</span> Two work related references have been obtained and verified.</li>
    <li style="top:736px"><span class="num">6.</span> An enhanced DBS Certificate has been provided.</li>
    <li style="top:782px"><span class="num">7.</span> In date, sufficient training certificates have been provided and verified or<br>in house training courses have been attended and certificates have been issued.</li>
    <li style="top:849px"><span class="num">8.</span> Registration with the appropriate bodies has been verified for Registered Nurses.</li>
    <li style="top:906px"><span class="num">9.</span> A shadow shift has been completed if it is a brand new staff member.</li>
    <li style="top:963px"><span class="num">10.</span> An ID Badge, uniform, and timesheets have been issued.</li>
  </ol>

  <p class="copy closing-a">We understand that it is imperative for our clients to only have extremely competent, fully trained staff supporting their existing team. We are proud to cover the standards set within the Care Certificate in the training modules that we deliver to our staff.</p>
  <p class="copy closing-b">All training is refreshed on an annual basis and we ensure that up to date certificates are held by all staff at all times.</p>

  <footer>
    <div class="footer-band"><div class="band-blue" style="width:461px"></div><div class="band-green"></div></div>
    <p class="footer-text">Registered in England No. 10483719 Carewell Staffline Services Ltd, 14 Orchard Row, Ashford, Kent, TN23 4QX</p>
  </footer>
</main>
</body>
</html>
```